New Wedding Decor Web Design Project - GUARANTEED PAYMENT

We need to have a business website for a brand new wedding decor & events company, Lirovelle. We have just established our logo and would love to use this logo on the website.

Because this is a new business venture, we do not have too many pictures to post online. It'd be exciting what your creativity can bring us!

Our website is: www.Lirovelle.ca

Target Market(s)

Our clientele demographic is targeted to brides and bridesmaids in their 20-30 years old.

Industry/Entity Type

Wedding

Requirements
Must have
• - Professional, elegant and artistic look
- Modern feeling
- Very catchy flash intro page
- Ability to show Chatterbook posts
Nice to have
• - Easy to navigate, crisp and clean
- Live vocaline messaging or online messaging

I would like to have navigation pages like: Lirovelle Brand, Collections, Features, Contact Us, etc.

Each page I want it to be clean and easy to read. Something like the following website: http://www.pardunetho.com/

We offer:
BACKDROPS
HEAD, CAKE & RECEIVING TABLES DECOR
CHAIRCOVERS
TABLE CLOTHS & OVERLAYS
NAPKINS
CENTREPIECES
CEREMONY SET-UP
CANDELABRA
CRYSTAL GLOBES
LED LIGHTING
CUSTOM DESIGN AISLE RUNNERS
CAKE STANDS
MONEY BOX
CHARGERS
GOBO LIGHTING
Should not have
• - traditional, old style website
- very static (dull)
- too many images or busy layout
- no "standardized" website templates such as: www.brintaq.com/gallery/weddings

```html
<!DOCTYPE html>
<html lang="en">
<head>
<meta charset="utf-8">
<title>Lirovelle — Wedding Decor &amp; Events</title>
<link href="https://fonts.googleapis.com/css2?family=Cinzel:wght@400;700&family=Libre+Baskerville:ital@1&family=PT+Sans+Narrow&display=swap" rel="stylesheet">
<style>
  :root {
    --page-bg: #f1ecee;
    --rule: #d6d0d2;
    --nav-text: #5f5a5c;
    --brand-rose: #d9368f;
    --brand-grey: #7a7a7a;
    --accent-red: #a5361f;
    --body-grey: #7b7677;
    --hero-warm: #b59f83;
    --thumb-border: #ffffff;
    --white: #ffffff;
    --social-blue: #2f66b3;
    --social-sky: #3fb1e4;
    --social-teal: #1f77a3;
    --social-dark: #3b3b3b;
  }
  * { margin: 0; padding: 0; box-sizing: border-box; }
  html, body { width: 1200px; height: 829px; overflow: hidden; }
  body {
    background: var(--page-bg);
    position: relative;
    font-family: "PT Sans Narrow", sans-serif;
    color: var(--nav-text);
  }
  .brand {
    position: absolute; left: 0; width: 1200px; top: 52px;
    display: flex; justify-content: center; align-items: center; gap: 10px;
  }
  .brand-dot { width: 26px; height: 26px; border-radius: 50%; background: var(--brand-rose); }
  .brand-name {
    font-family: "PT Sans Narrow", sans-serif; font-size: 44px; color: var(--brand-grey);
  }
  .double-rule {
    position: absolute; left: 180px; width: 840px; height: 4px;
    border-top: 1px solid var(--rule); border-bottom: 1px solid var(--rule);
  }
  .rule-top { top: 134px; }
  .rule-nav { top: 173px; }
  .rule-foot { top: 747px; }
  .main-nav {
    position: absolute; top: 148px; left: 188px; display: flex;
    font-size: 11.5px; text-transform: uppercase; letter-spacing: 0.2px;
  }
  .main-nav a { color: var(--nav-text); text-decoration: none; }
  .main-nav a + a { margin-left: 63px; }
  .search {
    position: absolute; left: 847px; top: 145px; width: 171px; height: 21px;
    background: var(--white); border: 1px solid var(--rule);
    font-family: Arial, sans-serif; font-size: 9.5px; color: #9c9899;
    padding: 5px 0 0 9px;
  }
  .search svg { position: absolute; right: 6px; top: 3px; }
  .hero {
    position: absolute; left: 180px; top: 184px; width: 840px; height: 453px;
    background: linear-gradient(180deg, #c9b69b 0%, #b09a7f 45%, #d8d2c8 100%);
  }
  .hero-photo { position: absolute; inset: 0 0 101px 0; background: linear-gradient(160deg, #cbb89c, #a99478 60%, #e4ded4); }
  .hero-title {
    position: absolute; left: 41px; top: 40px; color: var(--white);
    font-family: "Cinzel", serif;
  }
  .hero-title h1 { font-size: 44px; font-weight: 400; line-height: 1; }
  .hero-title p { font-size: 25px; line-height: 35px; margin-top: 4px; margin-left: 3px; }
  .hero-arrow { position: absolute; top: 164px; }
  .arrow-prev { left: 9px; }
  .arrow-next { right: 9px; }
  .thumbs {
    position: absolute; left: 7px; top: 353px; display: flex; gap: 8px;
  }
  .thumb { width: 160px; height: 96px; border: 2px solid var(--thumb-border); }
  .t1 { background: linear-gradient(160deg, #c8b79c, #a38f75); }
  .t2 { background: linear-gradient(160deg, #7a4fc9, #4b2a8c); }
  .t3 { background: linear-gradient(160deg, #8d8b8b, #3f3d3e); }
  .t4 { background: linear-gradient(160deg, #b89ad8, #6c3a8e); }
  .t5 { background: linear-gradient(160deg, #a39ad0, #6a6590); }
  .welcome {
    position: absolute; top: 653px; left: 180px; width: 840px; text-align: center;
  }
  .welcome h2 {
    font-family: "Cinzel", serif; font-weight: 400; font-size: 24px;
    color: var(--accent-red); letter-spacing: 0.5px;
  }
  .welcome p {
    font-family: "Libre Baskerville", serif; font-style: italic;
    font-size: 14px; line-height: 22px; color: var(--body-grey); margin-top: 6px;
  }
  .foot-nav {
    position: absolute; top: 769px; left: 189px; display: flex;
    font-size: 9.5px; text-transform: uppercase;
  }
  .foot-nav a { color: var(--nav-text); text-decoration: none; }
  .foot-nav .sep { margin: 0 15px; }
  .copyright {
    position: absolute; top: 789px; left: 189px; font-size: 8px; text-transform: uppercase;
  }
  .social-label {
    position: absolute; top: 775px; right: 308px; text-align: right;
    font-size: 8px; line-height: 12px; text-transform: uppercase;
  }
  .social { position: absolute; top: 770px; left: 899px; display: flex; gap: 3px; }
  .social span { width: 27px; height: 27px; border-radius: 50%; }
  .s1 { background: var(--social-blue); }
  .s2 { background: var(--social-sky); }
  .s3 { background: var(--social-teal); }
  .s4 { background: var(--social-dark); }
</style>
</head>
<body>
  <header class="brand">
    <span class="brand-dot"></span>
    <span class="brand-name">Lirovelle</span>
  </header>

  <div class="double-rule rule-top"></div>
  <nav class="main-nav">
    <a href="#">Home</a>
    <a href="#">Lirovelle Brand</a>
    <a href="#">Collections</a>
    <a href="#">Features</a>
    <a href="#">Contact Us</a>
  </nav>
  <div class="search">SEARCH :
    <svg width="16" height="14" viewBox="0 0 16 14"><circle cx="6" cy="6" r="4.2" fill="none" stroke="#bdb8b9" stroke-width="1.6"/><line x1="9" y1="9" x2="14" y2="12.5" stroke="#bdb8b9" stroke-width="2"/></svg>
  </div>
  <div class="double-rule rule-nav"></div>

  <section class="hero">
    <div class="hero-photo" role="img" aria-label="Banquet hall set with round tables, white chair covers and yellow floral centrepieces"></div>
    <div class="hero-title">
      <h1>LIROVELLE</h1>
      <p>WE ARE A WEDDING DECOR &amp;<br>EVENTS COMPANY</p>
    </div>
    <svg class="hero-arrow arrow-prev" width="40" height="40" viewBox="0 0 40 40"><circle cx="20" cy="20" r="17" fill="rgba(255,255,255,0.15)" stroke="#fff" stroke-width="2"/><path d="M23 11 L13 20 L23 29" fill="none" stroke="#fff" stroke-width="3"/></svg>
    <svg class="hero-arrow arrow-next" width="40" height="40" viewBox="0 0 40 40"><circle cx="20" cy="20" r="17" fill="rgba(255,255,255,0.15)" stroke="#fff" stroke-width="2"/><path d="M17 11 L27 20 L17 29" fill="none" stroke="#fff" stroke-width="3"/></svg>
    <div class="thumbs">
      <div class="thumb t1" role="img" aria-label="Banquet room with white table settings"></div>
      <div class="thumb t2" role="img" aria-label="Room lit with purple uplighting and draped cocktail tables"></div>
      <div class="thumb t3" role="img" aria-label="Long tables with grey runners and pink accents"></div>
      <div class="thumb t4" role="img" aria-label="Head table with draped backdrop in lilac light"></div>
      <div class="thumb t5" role="img" aria-label="Reception hall with round tables under violet lighting"></div>
    </div>
  </section>

  <section class="welcome">
    <h2>WELCOME TO LIROVELLE</h2>
    <p>We provide all these services Backdrops, Head, Cake &amp; Receiving Tables Décor, Chaircovers, Table Cloths &amp; Overlays, Nap-<br>kins, Crystal Globes, Led Lighting, Cake Stands</p>
  </section>

  <div class="double-rule rule-foot"></div>
  <footer>
    <nav class="foot-nav">
      <a href="#">Home</a><span class="sep">|</span>
      <a href="#">Lirovelle Brand</a><span class="sep">|</span>
      <a href="#">Collections</a><span class="sep">|</span>
      <a href="#">Features</a><span class="sep">|</span>
      <a href="#">Contact Us</a>
    </nav>
    <p class="copyright">Copyright © 2013 Lirovelle. All rights reserved.</p>
    <p class="social-label">Connect to<br>our social network :</p>
    <div class="social">
      <span class="s1"></span><span class="s2"></span><span class="s3"></span><span class="s4"></span>
    </div>
  </footer>
</body>
</html>
```